Poster & flyer for Charity Fashion Show

Using existing event graphic and supplied content, design a clean, eye catching A4 size poster and DLE size flyer for use in in shops, community noticeboards, cafes etc. Happy for the order of text to be moved around or in different placement for each. The *with celebrity MC Tobias Renwick-Hallam* section could be in a 'starburst' or similar type graphic anywhere on the poster/flyer (we are still awaiting final confirmation on the MC, so this content may change). If there is not enough room on the DLE size flyer, can leave off the sentence "Showcasing fabulous.....Op Shop Prices". If you require any other file formats for logos etc please just let me know.

```html
<!DOCTYPE html>
<html lang="en">
<head>
<meta charset="utf-8">
<title>Absolutely Fabulous Fashion Show</title>
<link rel="stylesheet" href="https://fonts.googleapis.com/css2?family=Montserrat:wght@200;700&family=Questrial&family=Roboto+Condensed:ital,wght@0,300;1,400;1,700&family=Kaushan+Script&display=swap">
<style>
  :root {
    --ink: #111111;
    --magenta: #c4137f;
    --paper: #ffffff;
  }
  * { margin: 0; padding: 0; box-sizing: border-box; }
  html, body { width: 1200px; height: 2470px; overflow: hidden; background: var(--paper); }
  .poster { position: relative; width: 1200px; height: 2470px; background: var(--paper); color: var(--ink); font-family: "Questrial", sans-serif; }
  .block { position: absolute; left: 0; width: 1200px; text-align: center; }

  .org-mark { position: absolute; left: 100px; top: 90px; display: flex; align-items: center; gap: 18px; }
  .org-mark .dot { width: 54px; height: 54px; border-radius: 50%; background: var(--ink); }
  .org-mark .org-name { font-family: "Questrial", sans-serif; font-size: 46px; color: var(--ink); line-height: 1; }

  .presents { top: 236px; font-family: "Kaushan Script", cursive; font-size: 56px; line-height: 1.1; padding-left: 40px; }

  .hanger-art { position: absolute; left: 84px; top: 330px; width: 1034px; height: 240px; }

  .title-top { top: 598px; display: flex; align-items: center; justify-content: center; gap: 30px; }
  .title-top .rule { width: 200px; height: 3px; background: var(--ink); }
  .title-top .word { font-family: "Montserrat", sans-serif; font-weight: 200; font-size: 78px; letter-spacing: 3px; line-height: 1; }

  .title-main { top: 672px; font-family: "Montserrat", sans-serif; font-weight: 700; font-size: 180px; color: var(--magenta); line-height: 1; }

  .title-sub { position: absolute; left: 106px; top: 820px; width: 990px; display: flex; align-items: center; gap: 22px; }
  .title-sub .bar { width: 570px; height: 24px; background: var(--ink); }
  .title-sub .label { font-family: "Montserrat", sans-serif; font-weight: 700; font-size: 40px; line-height: 1; white-space: nowrap; }

  .tagline { top: 900px; font-family: "Roboto Condensed", sans-serif; font-weight: 700; font-style: italic; font-size: 66px; line-height: 78px; color: var(--magenta); }
  .host { top: 1080px; font-family: "Kaushan Script", cursive; font-size: 46px; line-height: 56px; }

  .details { top: 1192px; font-size: 56px; line-height: 76px; }
  .tickets { top: 1585px; font-size: 50px; line-height: 70px; }
  .tickets .price { color: var(--magenta); }
  .fine-print { position: absolute; left: 168px; top: 1812px; width: 880px; font-family: "Roboto Condensed", sans-serif; font-style: italic; font-size: 28px; line-height: 35px; text-align: left; }

  .showcase { top: 1975px; font-family: "Roboto Condensed", sans-serif; font-weight: 700; font-style: italic; font-size: 58px; line-height: 76px; }
  .footer { top: 2292px; font-family: "Roboto Condensed", sans-serif; font-weight: 300; font-size: 29px; letter-spacing: 0.5px; text-transform: uppercase; }
</style>
</head>
<body>
<main class="poster">
  <div class="org-mark">
    <span class="dot"></span>
    <span class="org-name">Westgate Hospice</span>
  </div>

  <p class="block presents">Presents</p>

  <svg class="hanger-art" viewBox="0 0 1034 240" role="img" aria-label="Clothes hanger with a question-mark hook, covered in a pink and yellow lily floral pattern">
    <defs>
      <linearGradient id="floral" x1="0" y1="0" x2="1" y2="0">
        <stop offset="0" stop-color="#f7c6de"/>
        <stop offset="0.35" stop-color="#e2479a"/>
        <stop offset="0.6" stop-color="#c8e59a"/>
        <stop offset="0.85" stop-color="#f4d23a"/>
        <stop offset="1" stop-color="#e9f3d5"/>
      </linearGradient>
    </defs>
    <rect x="0" y="0" width="1034" height="240" rx="60" fill="url(#floral)" opacity="0.85"/>
  </svg>

  <div class="block title-top">
    <span class="rule"></span>
    <span class="word">ABSOLUTELY</span>
    <span class="rule"></span>
  </div>
  <h1 class="block title-main">FABULOUS</h1>
  <div class="title-sub">
    <span class="bar"></span>
    <span class="label">FASHION SHOW</span>
  </div>

  <p class="block tagline">“A night of upcycled fashion, beauty,<br>auctions and entertainment”</p>
  <p class="block host">“with celebrity MC Tobias Renwick-Hallam”</p>

  <p class="block details">Thursday 21 August 2014,<br>7.30pm<br>Harbourview on Kauri<br>42 Kauri Rd, Glendene<br>Auckland</p>

  <p class="block tickets"><span class="price">Tickets* $49 or $60VIP</span><br>Tickets strictly limited - book online at<br>tixline.co.nz or ph (09) 555 0142</p>

  <p class="fine-print">All tickets include complimentary canapés &amp; a glass of bubbles<br>VIP tickets include a Goodie Bag and reserved seating (front two rows)<br>*+ booking fee</p>

  <p class="block showcase">“Showcasing fabulous upcycled fashion<br>from Westgate Charity Shops - all garments<br>available for sale on the night at Op<br>Shop prices!”</p>

  <p class="block footer">All proceeds to Westgate Hospice’s new specialist palliative care unit</p>
</main>
</body>
</html>
```